Boutique growth strategy brochure

This may be a larger task than a traditional brochure. This is a brochure I had made up for my old company. I always liked it and it replicated my website ( although the website had more content). What I would like to do is make a similar brochure as far as style goes and I would also like to incorporate the same information into a new website. Some of the wording will need to be changed as well as the Company name and Logo. Is this something that you would be interested in working on ( Bothe the brochure and a website?)

Regards,
Brent

Target Market(s)

Mid sized business owners

Industry/Entity Type

Mid sized privately owned businesses largely service oriented

Colors

Designer to choose colors to be used in the design.

Requirements
Must have
• Professional look and feel
Nice to have
• This was a design from an old folder. I want to create something similar with the new company name (Harborline Venture Partners) or HVP logo

```html
<!DOCTYPE html>
<html lang="en">
<head>
<meta charset="utf-8">
<title>HVP Services – Harborline Venture Partners</title>
<link href="https://fonts.googleapis.com/css2?family=Poppins:wght@500;600;700&family=Kurale&display=swap" rel="stylesheet">
<style>
  :root{
    --navy:#002d47;
    --ring:#1e3d57;
    --hub-ring:#4b5a6e;
    --ink:#0b1b29;
    --white:#ffffff;
    --exit:#ef5438;
    --growth:#f7991f;
    --sales:#e2c323;
    --comms:#8cc542;
    --special:#37bcad;
    --bizdev:#00abcc;
    --outsource:#0a7f99;
    --risk:#804283;
    --mergers:#b81e7a;
  }
  html,body{margin:0;padding:0;overflow:hidden;}
  body{width:1200px;height:776px;position:relative;background:var(--white);font-family:"Poppins",sans-serif;}
  .services-panel{position:absolute;left:0;top:0;width:600px;height:776px;background:var(--navy);}
  .services-title{position:absolute;left:33px;top:68px;margin:0;color:var(--white);font-family:"Poppins",sans-serif;font-weight:500;font-size:24px;letter-spacing:.5px;}
  .service-wheel{position:absolute;left:0;top:0;}
  .wedge-label{font-family:"Poppins",sans-serif;font-weight:600;font-size:12.5px;fill:var(--white);}
  .hub-name{font-family:"Poppins",sans-serif;font-weight:700;font-size:10.5px;fill:var(--ink);letter-spacing:.6px;}
  .about{position:absolute;left:705px;top:0;width:420px;color:var(--ink);}
  .about h2{position:absolute;left:0;margin:0;font-family:"Poppins",sans-serif;font-weight:700;font-size:24px;letter-spacing:.4px;white-space:nowrap;}
  .about p{position:absolute;left:0;margin:0;font-family:"Kurale",serif;font-size:19.5px;line-height:23.7px;white-space:nowrap;}
  .mission-title{top:124px;}
  .mission-text{top:164px;}
  .vision-title{top:311px;}
  .vision-text{top:347px;}
  .contact{position:absolute;left:705px;top:589px;color:var(--ink);}
  .contact-intro{margin:0;font-family:"Kurale",serif;font-size:14px;line-height:18px;}
  .contact-email{margin:10px 0 0;font-family:"Poppins",sans-serif;font-weight:600;font-size:11.5px;}
  .contact-phone{margin:4px 0 0;font-family:"Kurale",serif;font-size:14px;}
  .contact-phone strong{font-family:"Poppins",sans-serif;font-weight:600;font-size:11.5px;}
  .footer-mark{position:absolute;left:1076px;top:724px;display:flex;align-items:center;gap:5px;color:var(--ink);}
  .footer-mark .mark-square{width:14px;height:14px;background:var(--ink);}
  .footer-mark .mark-name{font-family:"Poppins",sans-serif;font-weight:700;font-size:6.5px;line-height:7px;letter-spacing:.4px;}
</style>
</head>
<body>
  <section class="services-panel">
    <h1 class="services-title">HVP SERVICES</h1>
    <svg class="service-wheel" width="600" height="776" viewBox="0 0 600 776">
      <defs>
        <radialGradient id="hubFace" cx="35%" cy="30%" r="75%">
          <stop offset="0" stop-color="#ffffff"/>
          <stop offset="1" stop-color="#e4e4e4"/>
        </radialGradient>
      </defs>
      <!-- outer track -->
      <circle cx="305" cy="413" r="261" fill="none" stroke="var(--ring)" stroke-width="2.5"/>
      <circle cx="305" cy="413" r="137" fill="none" stroke="var(--ring)" stroke-width="2"/>
      <g class="wedges" stroke="var(--navy)" stroke-width="10" stroke-linejoin="round">
        <path fill="var(--exit)" d="M305 163 A250 250 0 0 1 465.7 221.5 L387.3 315 A128 128 0 0 0 305 285 Z"/>
        <path fill="var(--growth)" d="M465.7 221.5 A250 250 0 0 1 551.2 369.6 L431.1 390.8 A128 128 0 0 0 387.3 315 Z"/>
        <path fill="var(--sales)" d="M551.2 369.6 A250 250 0 0 1 521.5 538 L415.8 477 A128 128 0 0 0 431.1 390.8 Z"/>
        <path fill="var(--comms)" d="M521.5 538 A250 250 0 0 1 390.5 647.9 L348.8 533.3 A128 128 0 0 0 415.8 477 Z"/>
        <path fill="var(--special)" d="M390.5 647.9 A250 250 0 0 1 219.5 647.9 L261.2 533.3 A128 128 0 0 0 348.8 533.3 Z"/>
        <path fill="var(--bizdev)" d="M219.5 647.9 A250 250 0 0 1 88.5 538 L194.2 477 A128 128 0 0 0 261.2 533.3 Z"/>
        <path fill="var(--outsource)" d="M88.5 538 A250 250 0 0 1 58.8 369.6 L178.9 390.8 A128 128 0 0 0 194.2 477 Z"/>
        <path fill="var(--risk)" d="M58.8 369.6 A250 250 0 0 1 144.3 221.5 L222.7 315 A128 128 0 0 0 178.9 390.8 Z"/>
        <path fill="var(--mergers)" d="M144.3 221.5 A250 250 0 0 1 305 163 L305 285 A128 128 0 0 0 222.7 315 Z"/>
      </g>
      <!-- track nodes -->
      <g class="track-nodes" fill="var(--navy)" stroke="#41566c" stroke-width="1.5">
        <circle cx="305" cy="152" r="3.5"/><circle cx="472.8" cy="213" r="3.5"/>
        <circle cx="562" cy="367.7" r="3.5"/><circle cx="531" cy="543.5" r="3.5"/>
        <circle cx="394.3" cy="658.3" r="3.5"/><circle cx="215.7" cy="658.3" r="3.5"/>
        <circle cx="79" cy="543.5" r="3.5"/><circle cx="48" cy="367.7" r="3.5"/>
        <circle cx="137.2" cy="213" r="3.5"/>
        <circle cx="305" cy="294" r="3.5"/><circle cx="381" cy="322" r="3.5"/>
        <circle cx="422" cy="392" r="3.5"/><circle cx="408" cy="472" r="3.5"/>
        <circle cx="346" cy="524" r="3.5"/><circle cx="264" cy="524" r="3.5"/>
        <circle cx="202" cy="472" r="3.5"/><circle cx="188" cy="392" r="3.5"/>
        <circle cx="229" cy="322" r="3.5"/>
      </g>
      <!-- hub -->
      <circle cx="305" cy="413" r="109" fill="var(--hub-ring)"/>
      <circle cx="305" cy="413" r="90" fill="url(#hubFace)"/>
      <rect x="236" y="398" width="10" height="10" fill="var(--ink)"/>
      <text class="hub-name" x="252" y="397">HARBORLINE</text>
      <text class="hub-name" x="252" y="409">VENTURE</text>
      <text class="hub-name" x="252" y="421">PARTNERS</text>
      <!-- service icon spots -->
      <g class="icon-spots" fill="#ffffff" fill-opacity=".2">
        <circle role="img" aria-label="Door with exit arrow icon" cx="370" cy="219" r="17"/>
        <circle role="img" aria-label="Rising hero with growth arrows icon" cx="464" cy="297" r="17"/>
        <circle role="img" aria-label="Megaphone icon" cx="494" cy="427" r="17"/>
        <circle role="img" aria-label="Team conversation icon" cx="434" cy="540" r="17"/>
        <circle role="img" aria-label="Checklist clipboard icon" cx="306" cy="582" r="17"/>
        <circle role="img" aria-label="Rising bar chart icon" cx="181" cy="540" r="17"/>
        <circle role="img" aria-label="Globe and people icon" cx="126" cy="432" r="17"/>
        <circle role="img" aria-label="Warning sign under magnifier icon" cx="144" cy="292" r="17"/>
        <circle role="img" aria-label="Handshake with dollar icon" cx="241" cy="216" r="17"/>
      </g>
      <g class="wedge-labels">
        <text class="wedge-label" x="373" y="258" text-anchor="middle">Exit Strategies</text>
        <text class="wedge-label" x="476" y="338" text-anchor="middle"><tspan x="481">Growth</tspan><tspan x="476" dy="13">Solutions</tspan></text>
        <text class="wedge-label" x="491" y="468" text-anchor="middle"><tspan x="494">Sales &amp;</tspan><tspan x="491" dy="13">Marketing</tspan></text>
        <text class="wedge-label" x="436" y="579" text-anchor="middle">Communications</text>
        <text class="wedge-label" x="304" y="623" text-anchor="middle"><tspan x="302">Special</tspan><tspan x="304" dy="13">Projects</tspan></text>
        <text class="wedge-label" x="140" y="577"><tspan x="140">Business</tspan><tspan x="140" dy="13">Development</tspan></text>
        <text class="wedge-label" x="125" y="470" text-anchor="middle">Outsourcing</text>
        <text class="wedge-label" x="97" y="327"><tspan x="97">Risk</tspan><tspan x="97" dy="13">Management</tspan></text>
        <text class="wedge-label" x="210" y="253"><tspan x="210">Mergers &amp;</tspan><tspan x="210" dy="13">Acquisitions</tspan></text>
      </g>
    </svg>
  </section>

  <section class="about">
    <h2 class="mission-title">OUR MISSION</h2>
    <p class="mission-text">To provide professional solutions that<br>allow our partners and clients to not only<br>meet but exceed their objectives using<br>“Customer Vision”.</p>
    <h2 class="vision-title">CUSTOMER VISION</h2>
    <p class="vision-text">We see your business and needs through<br>your eyes to work together for the<br>ultimate solution.</p>
  </section>

  <section class="contact">
    <p class="contact-intro">Contact us to arrange a discreet meeting to discuss your<br>objectives and requirements.</p>
    <p class="contact-email">inquiry@harborlinevp.com</p>
    <p class="contact-phone">Phone <strong>555.014.2290</strong></p>
  </section>

  <div class="footer-mark">
    <span class="mark-square"></span>
    <span class="mark-name">HARBORLINE<br>VENTURE<br>PARTNERS</span>
  </div>
</body>
</html>
```